Wine Label for a White and a Red Wine from Italy

We have a very good idea of what we want with artwork. We need you to please design a 'template' with the text so we can change out the artwork from year to year. Samples are shown of what we are looking for. We are looking for options with the two basic designs. Brand name of wine is: Valora di Castegno. Both wines are in a light green Bordeaux-style bottle (note: we don't show a light green bottle in the mockup but please remember the bottle is light green). Artwork is provided. We'd like to see either the green or blue butterfly on the white wine, the red butterfly is for the red wine. Please base the design on the attached label from Brailey and/or the attached label from Chateau Mervanges.

Target Market(s)

Millennials, women

Requirements
Must have
• The artwork (butterflies) attached.
Nice to have
• Elegant, readable fonts. Please make the text so it can be changed by the printer. Please make it so the artwork can be changed too.

```html
<!DOCTYPE html>
<html lang="en">
<head>
<meta charset="utf-8">
<title>Valora di Castegno – Barrel Select Labels</title>
<link href="https://fonts.googleapis.com/css2?family=Cormorant+Garamond:wght@400;500;600&display=swap" rel="stylesheet">
<style>
  :root {
    --page-bg: #f4f5e8;
    --label-paper: #efefe7;
    --label-edge: #dcdcd2;
    --ink: #2a2a2a;
    --ink-soft: #4a4a48;
    --rosso-gold: #f3b21c;
    --rosso-amber: #e98a12;
    --rosso-red: #a8261c;
    --bianco-leaf: #a9c48a;
    --bianco-moss: #4f6f45;
    --bianco-stone: #c9c3b2;
  }
  * { box-sizing: border-box; margin: 0; padding: 0; }
  html, body {
    width: 1200px; height: 1200px; overflow: hidden;
    background: var(--page-bg);
  }
  .canvas {
    position: relative;
    width: 1200px; height: 1200px;
    font-family: "Cormorant Garamond", Georgia, serif;
    color: var(--ink);
  }
  .wine-label {
    position: absolute;
    top: 260px;
    width: 470px; height: 680px;
    background: var(--label-paper);
    border: 1px solid var(--label-edge);
    text-align: center;
  }
  .wine-label--rosso { left: 100px; }
  .wine-label--bianco { left: 630px; }
  .wine-label > * { position: absolute; left: 0; right: 0; }

  .brand-name {
    top: 34px;
    font-size: 64px; font-weight: 500;
    letter-spacing: 6px; line-height: 1;
  }
  .brand-sub {
    top: 112px;
    font-size: 34px; font-weight: 500; line-height: 1;
    color: var(--ink-soft);
  }
  .range-name {
    top: 172px;
    font-size: 22px; font-weight: 500;
    letter-spacing: 6px; line-height: 1;
    color: var(--ink-soft);
  }
  .artwork {
    top: 195px;
    left: 60px; right: 60px;
    height: 320px;
    border-radius: 46% 40% 48% 38% / 40% 46% 38% 50%;
  }
  .wine-label--rosso .artwork {
    background:
      radial-gradient(ellipse 38% 28% at 42% 46%, var(--rosso-red) 0%, rgba(168,38,28,0.7) 55%, rgba(168,38,28,0) 100%),
      radial-gradient(ellipse 60% 55% at 55% 45%, var(--rosso-gold) 0%, var(--rosso-amber) 60%, rgba(233,138,18,0) 100%);
  }
  .wine-label--bianco .artwork {
    left: 85px; right: 85px;
    background:
      radial-gradient(ellipse 40% 32% at 45% 50%, var(--bianco-moss) 0%, rgba(79,111,69,0.6) 55%, rgba(79,111,69,0) 100%),
      radial-gradient(ellipse 60% 55% at 50% 45%, var(--bianco-leaf) 0%, var(--bianco-stone) 65%, rgba(201,195,178,0) 100%);
  }
  .vintage {
    top: 498px;
    font-size: 30px; font-weight: 500;
    letter-spacing: 4px; line-height: 1;
  }
  .wine-type {
    top: 546px;
    font-size: 36px; font-weight: 600;
    letter-spacing: 6px; line-height: 1;
  }
  .origin {
    top: 590px;
    font-size: 32px; font-weight: 500;
    letter-spacing: 2px; line-height: 1;
    color: var(--ink-soft);
  }
  .producer {
    top: 626px;
    font-size: 14px; font-weight: 500;
    letter-spacing: 1px; line-height: 1;
    color: var(--ink-soft);
  }
  .farming-note {
    top: 652px;
    font-size: 17px; font-weight: 500;
    letter-spacing: 1px; line-height: 1;
    color: var(--ink-soft);
  }
</style>
</head>
<body>
<main class="canvas">

  <section class="wine-label wine-label--rosso">
    <h1 class="brand-name">VALORA</h1>
    <p class="brand-sub">di Castegno</p>
    <div class="artwork" role="img" aria-label="Red butterfly painted over broad yellow and orange brush strokes"></div>
    <p class="range-name">BARREL SELECT</p>
    <p class="vintage">2018</p>
    <p class="wine-type">ROSSO</p>
    <p class="origin">Piemonte Italy</p>
    <p class="producer">Artisanally Crafted by Cantina Sette Colli</p>
    <p class="farming-note">sustainably farmed</p>
  </section>

  <section class="wine-label wine-label--bianco">
    <h1 class="brand-name">VALORA</h1>
    <p class="brand-sub">di Castegno</p>
    <div class="artwork" role="img" aria-label="Green butterfly painted in loose green and stone-grey brush strokes"></div>
    <p class="range-name">BARREL SELECT</p>
    <p class="vintage">2018</p>
    <p class="wine-type">BIANCO</p>
    <p class="origin">Piemonte Italy</p>
    <p class="producer">Artisanally Crafted by Cantina Sette Colli</p>
    <p class="farming-note">sustainably farmed</p>
  </section>

</main>
</body>
</html>
```